Real Estate Investor needs awesome business card design

I invest in real estate, focused on multi-family properties, and I need a business card to hand out to potential partners. I prefer simple, clean designs, but it needs to stand out, so I'd like there to be a bit of red in the design as well.

It should include this information:

Front
Calder Whitby
Real Estate Investor
Direct phone: 501-555-0187
Email: calderjwhitby@mailbox-example.net
Headshot (Picture), I've uploaded a few, just pick the one you think looks best with your design. You can remove the background from the headshot image if it looks better.

Back
The back of the card's design should flow and be congruent with the front. On the back I want to put an inspirational quote or question. There will be different ones depending on the card, so I'll need the original file so I can edit it in the end.

For now, use “The Pessimist Sees Difficulty In Every Opportunity. The Optimist Sees The Opportunity In Every Difficulty.” -Edmund Halvorsen

Target Market(s)

Investors

Industry/Entity Type

Real Estate

Contact Information for Business Card

Front
Calder Whitby
Real Estate Investor

Back
The back of the card's design should flow and be congruent with the front. On the back I want to put an inspirational quote or question. There will be different ones depending on the card, so I'll need the original file so I can edit it in the end. I've uploaded some EXAMPLES of business cards with quotes on them. Don't copy but feel free to use them as inspiration.

The design will be printed on "ZAP sized" business cards
1039 x 697 pixels
with rounded corners

Font styles to use
Serif
Decorative
Script

Colors
ec1f27

Requirements
Must have
• Headshot, name, and other information in it.
• 1039 x 697 pixels
• Rounded corners
• Clean design that pops. I'm open to see any color background, including black.
• Headshots can be located here: https://www.filecrate-example.com/sh/8kx2vq71ld0pa3z/BQQTXL7mrrf9eT3Kq0HhgkLm2b?dl=0
Nice to have
• It would be awesome if the design included a personal signature or monogram, but if not I'll get a personal logo developed later and the card redesigned if I think it needs it.
Should not have
• Cluttered design

```html
<!DOCTYPE html>
<html lang="en">
<head>
<meta charset="utf-8">
<title>Calder Whitby — Business Card</title>
<link rel="stylesheet" href="https://fonts.googleapis.com/css2?family=Gelasio:wght@400&family=Cinzel:wght@400;500&display=swap">
<style>
  :root {
    --page: #e9e6e2;
    --card-white: #ffffff;
    --ink: #000000;
    --accent: #ec1f27;
    --light-text: #ffffff;
    --photo-tone-a: #d9d9d9;
    --photo-tone-b: #3a3a3a;
  }
  html, body {
    margin: 0;
    padding: 0;
    width: 1200px;
    height: 966px;
    overflow: hidden;
    background: var(--page);
  }
  .sheet {
    position: relative;
    width: 1200px;
    height: 966px;
  }
  .card {
    position: absolute;
    left: 272px;
    width: 656px;
    height: 397px;
    border-radius: 16px;
    overflow: hidden;
    box-shadow: 0 6px 14px rgba(0,0,0,0.18);
  }
  .card--front { top: 52px; background: var(--card-white); }
  .card--back  { top: 495px; background: var(--ink); }

  .front-band {
    position: absolute;
    left: 0;
    top: 128px;
    width: 440px;
    height: 142px;
    background: var(--ink);
  }
  .front-accent {
    position: absolute;
    left: 570px;
    top: 128px;
    width: 86px;
    height: 142px;
    background: var(--accent);
  }
  .headshot {
    position: absolute;
    left: 398px;
    top: 96px;
    width: 204px;
    height: 204px;
  }
  .identity {
    position: absolute;
    left: 44px;
    top: 152px;
    font-family: "Gelasio", Georgia, serif;
    color: var(--light-text);
  }
  .identity__name {
    margin: 0;
    font-size: 24px;
    line-height: 26px;
    font-weight: 400;
    color: var(--accent);
  }
  .identity__role {
    margin: 0 0 10px;
    font-size: 17px;
    line-height: 22px;
  }
  .identity__contact {
    margin: 0;
    font-size: 17px;
    line-height: 22px;
  }
  .identity__label { color: var(--accent); }

  .quote {
    position: absolute;
    left: 100px;
    top: 62px;
    margin: 0;
    font-family: "Cinzel", "Trajan Pro", serif;
    color: var(--light-text);
  }
  .quote__text {
    margin: 0 0 8px;
    font-size: 30px;
    line-height: 34px;
    font-weight: 500;
  }
  .quote__text span { display: block; }
  .quote__text .quote__gap { margin-top: 2px; }
  .quote__author {
    margin: 0;
    font-size: 33px;
    line-height: 37px;
    font-weight: 400;
    color: var(--accent);
  }
  .quote__author span { display: block; }
</style>
</head>
<body>
<main class="sheet">
  <section class="card card--front" aria-label="Card front">
    <div class="front-band"></div>
    <div class="front-accent"></div>
    <svg class="headshot" viewBox="0 0 204 204" role="img" aria-label="Black and white headshot of Calder Whitby">
      <defs>
        <linearGradient id="photoTone" x1="0" y1="0" x2="0" y2="1">
          <stop offset="0" stop-color="var(--photo-tone-a)"/>
          <stop offset="1" stop-color="var(--photo-tone-b)"/>
        </linearGradient>
      </defs>
      <circle cx="102" cy="102" r="101" fill="#ffffff" stroke="#ec1f27" stroke-width="2"/>
      <circle cx="102" cy="102" r="96" fill="url(#photoTone)" stroke="#ec1f27" stroke-width="1.5"/>
    </svg>
    <div class="identity">
      <h1 class="identity__name">Calder Whitby</h1>
      <p class="identity__role">Real Estate Investor</p>
      <p class="identity__contact"><span class="identity__label">P:</span> 501-555-0187</p>
      <p class="identity__contact"><span class="identity__label">E:</span> calderjwhitby@mailbox-example.net</p>
    </div>
  </section>

  <section class="card card--back" aria-label="Card back">
    <figure class="quote">
      <blockquote class="quote__text">
        <span>The Pessimist Sees Dif-</span>
        <span>ficulty In Every Op-</span>
        <span>portunity.</span>
        <span class="quote__gap">The Optimist Sees</span>
        <span>The Opportunity In</span>
        <span>Every Difficulty.</span>
      </blockquote>
      <figcaption class="quote__author"><span>Edmund</span><span>Halvorsen</span></figcaption>
    </figure>
  </section>
</main>
</body>
</html>
```